Helicopter Company - Skyvane Sweden

I need a new design and implementation of a webpage. We rent helicopters and are also starting a school. We havre started a wordpress but the page is very ugly. Need a complete update. Logo exist already. We also have some pictures of helicotopers. We are open for all designs but it is important that it looks professionel, is eassy to update and will give an impression och structure and dicipline.
Updates

Target Market(s)

Customers that what to get a certificate to fly. It is expensive so it’s either people with a lot of money or people with a big dream. It is very serious business.

Industry/Entity Type

www.skyvane-demo.se

Coding

Coded - Design and coding required

Number of Pages Required

4 page

Font styles to use
Sans Serif

Colors
0054AA
0677BA
7BADD7
CADEEF
E8F1F8

Requirements
Must have
• A easy page the gives a feeling of seriousness and

```html
<!DOCTYPE html>
<html lang="sv">
<head>
<meta charset="utf-8">
<title>Skyvane – Uthyrning av helikopter</title>
<link rel="stylesheet" href="https://fonts.googleapis.com/css2?family=Domine:wght@400;700&family=Montserrat:wght@400;500;600;700;900&display=swap">
<style>
  :root {
    --ink: #111111;
    --text: #3a3a3a;
    --muted: #777777;
    --teal: #2a8f8c;
    --orange: #e8872d;
    --topbar: #f3f3f3;
    --grey-block: #b9b9b9;
    --grey-text: #d8d8d8;
    --footer: #333333;
    --footer-text: #e6e6e6;
    --footer-line: #4d4d4d;
    --white: #ffffff;
  }
  * { margin: 0; padding: 0; box-sizing: border-box; }
  html, body { width: 676px; height: 1200px; overflow: hidden; }
  body { position: relative; background: var(--white); font-family: "Montserrat", sans-serif; color: var(--text); }
  .abs { position: absolute; }

  .topbar { left: 0; top: 0; width: 676px; height: 24px; background: var(--topbar); }
  .contact-item { top: 5px; display: flex; align-items: center; gap: 6px; font-size: 7.5px; color: var(--ink); }
  .contact-item .dot { width: 14px; height: 14px; border-radius: 50%; background: var(--teal); display: flex; align-items: center; justify-content: center; }
  .social { top: 5px; width: 15px; height: 15px; border-radius: 50%; background: #9b9b9b; }

  .site-header { left: 0; top: 24px; width: 676px; height: 42px; background: var(--white); }
  .brand { left: 90px; top: 11px; font-family: "Domine", serif; font-size: 22px; letter-spacing: 0.5px; color: var(--ink); display: flex; align-items: center; gap: 6px; }
  .brand .mark { width: 9px; height: 9px; border-radius: 50%; background: var(--ink); }
  .nav a { position: absolute; top: 19px; font-size: 7.3px; color: var(--ink); text-decoration: none; letter-spacing: 0.2px; }
  .nav a.active { color: var(--teal); font-weight: 600; }

  .hero { left: 0; top: 66px; width: 676px; height: 169px;
    background: linear-gradient(180deg, #c9d6de 0%, #dfe6e6 35%, #7fa35a 52%, #5f9a3a 70%, #7ab04a 100%); }
  .hero-title { left: 91px; top: 110px; font-weight: 900; font-size: 27px; line-height: 33px; color: var(--ink); letter-spacing: 0.5px; }
  .crumbs { left: 91px; top: 178px; font-size: 7.5px; color: var(--ink); }
  .crumbs b { font-weight: 700; margin-left: 4px; }

  .section-title { left: 0; width: 676px; top: 300px; text-align: center; font-family: "Domine", serif; font-size: 24px; font-weight: 400; color: var(--ink); letter-spacing: 0.4px; }

  .grey-block { background: var(--grey-block); }
  .vertical { font-family: "Domine", serif; color: var(--grey-text); white-space: nowrap; line-height: 22px; }

  .photo-frame { border: 2px solid var(--white); }
  .photo { width: 100%; height: 100%; }

  .body-copy { font-size: 7.2px; line-height: 13px; text-align: justify; color: var(--text); }
  .body-copy h3 { font-size: 8px; font-weight: 700; color: var(--ink); margin-bottom: 6px; text-align: left; }
  .body-copy p { margin-bottom: 4px; }

  .fleet-title { left: 91px; top: 752px; font-family: "Domine", serif; font-size: 25px; line-height: 33px; color: var(--ink); letter-spacing: 0.6px; }
  .fleet-copy { left: 91px; top: 850px; width: 240px; font-size: 7.3px; line-height: 13px; }
  .fleet-copy h3 { font-size: 7.6px; font-weight: 700; color: var(--ink); margin-bottom: 5px; }
  .btn { left: 92px; top: 912px; width: 139px; height: 25px; border: 1.5px solid var(--orange); color: var(--orange); font-size: 8px; font-weight: 600; display: flex; align-items: center; justify-content: center; }

  .site-footer { left: 0; top: 1032px; width: 676px; height: 168px; background: var(--footer); color: var(--footer-text); }
  .f-col { position: absolute; top: 40px; font-size: 7.5px; line-height: 11px; }
  .f-col h4 { font-size: 13px; font-weight: 500; margin-bottom: 8px; color: var(--white); }
  .f-col li { list-style: none; margin-bottom: 9.5px; }
  .f-contact { display: flex; align-items: center; gap: 6px; margin-bottom: 9px; }
  .f-contact .dot { width: 15px; height: 15px; border-radius: 50%; background: var(--teal); flex: none; display: flex; align-items: center; justify-content: center; }
  .f-contact b { font-weight: 700; display: block; }
  .f-rule { position: absolute; left: 91px; top: 139px; width: 494px; height: 1px; background: var(--footer-line); }
  .copyright { position: absolute; left: 91px; top: 149px; font-size: 7.3px; }
  .f-social { position: absolute; top: 147px; width: 15px; height: 15px; border-radius: 50%; background: #9b9b9b; }
  .f-social.blue { background: #1a6fd1; }
</style>
</head>
<body>

  <div class="abs topbar">
    <div class="abs contact-item" style="left:90px">
      <span class="dot"><svg width="8" height="8" viewBox="0 0 24 24"><path fill="#fff" d="M6.6 10.8a15.1 15.1 0 0 0 6.6 6.6l2.2-2.2a1 1 0 0 1 1-.25 11.4 11.4 0 0 0 3.6.57 1 1 0 0 1 1 1V20a1 1 0 0 1-1 1A17 17 0 0 1 3 4a1 1 0 0 1 1-1h3.5a1 1 0 0 1 1 1c0 1.25.2 2.45.57 3.57a1 1 0 0 1-.25 1z"/></svg></span>
      +46 700 123 456
    </div>
    <div class="abs contact-item" style="left:190px">
      <span class="dot"><svg width="8" height="8" viewBox="0 0 24 24"><path fill="none" stroke="#fff" stroke-width="2.4" d="M3 6h18v12H3zM3 6l9 7 9-7"/></svg></span>
      info@skyvane-demo.se
    </div>
    <div class="abs social" style="left:548px"></div>
    <div class="abs social" style="left:569px"></div>
  </div>

  <header class="abs site-header">
    <div class="abs brand"><span class="mark"></span>Skyvane</div>
    <nav class="nav">
      <a style="left:255px">HEM</a>
      <a class="active" style="left:291px">UTHYRNING AV HELIKOPTER</a>
      <a style="left:426px">HELIKOPTERSKOLA</a>
      <a style="left:523px">KONTAKTA OSS</a>
    </nav>
  </header>

  <section class="abs hero" role="img" aria-label="Helikopter parkerad på ett grönt gräsfält under en ljus himmel"></section>
  <h1 class="abs hero-title">UTHYRNING AV<br>HELIKOPTER</h1>
  <div class="abs crumbs">Hem &nbsp;»<b>UTHYRNING AV HELIKOPTER</b></div>

  <h2 class="abs section-title">HYR HELIKOPTER AV OSS!</h2>

  <div class="abs grey-block" style="left:0;top:359px;width:154px;height:288px"></div>
  <div class="abs vertical" style="left:25px;top:630px;transform:rotate(-90deg);transform-origin:left top;font-size:24px;width:260px">Hyr Helikopter Av<br><span style="padding-left:150px">Oss!</span></div>
  <div class="abs photo-frame" style="left:90px;top:381px;width:239px;height:228px">
    <div class="photo" role="img" aria-label="Hand som håller upp ett vitt dokument mot beige bakgrund" style="background:linear-gradient(135deg,#ecc9a0,#e9c49a 60%,#dcb48a)"></div>
  </div>
  <div class="abs body-copy" style="left:356px;top:380px;width:230px">
    <h3>Time-building eller nöjesflygning?</h3>
    <p>Hos oss kan ni hyra helikopter i skåne. Egentligen kan ni hyra den var som helst och vi har till och med leverans av helikopter. Vill ni ha den framflygen står vi för piloten och hens transport samt logi. Du står bara för själva kostnaden av helikoptern.</p>
    <p>Vi utgår från ESXN, Norrviks flygfält, ett flygfält som är stort, lättillgänligt och väldigt bra att flyga till och från. Vi tar alltid en deposition, eller snarare behöver ni göra en inbetalning av ett antal timmar för att kunna täcka upp för eventuella oförutsedda avgifter.</p>
    <p>Innan ni får hyra vill i se alla era dokument, medical och certificat och även titta i loggboken. Sedan flyger vi en runda tillsammans och går igenom den maskin ni ska hyra. Det kanske viktigaste för oss är att vi först träffas, dricker en kaffe (eller te, eller nått) för att få en känsla för varandra. Vi är ett litet bolag som vill ha nära kontakt med våra kunder.</p>
  </div>

  <h2 class="abs fleet-title">VI ANVÄNDER JUS<br>NU HELIKOPTER<br>ROTORLINE R40.</h2>
  <div class="abs fleet-copy">
    <h3>En fantastisk maskin till rimligt pris!</h3>
    <p>Du kan läsa mer om just våra helikoptrar i skåne genom att klicka på längen nedanför.</p>
  </div>
  <a class="abs btn">Läs mer om våra helikoptrar!</a>

  <div class="abs grey-block" style="left:479px;top:698px;width:197px;height:288px"></div>
  <div class="abs vertical" style="left:667px;top:712px;transform:rotate(90deg);transform-origin:left top;font-size:17px;width:260px">VI ANVÄNDER JUST NU<br>HELIKOPTER ROTORLINE R40.</div>
  <div class="abs photo-frame" style="left:347px;top:719px;width:240px;height:229px">
    <div class="photo" role="img" aria-label="Mörk helikopter i en ljus hangar" style="background:linear-gradient(180deg,#d8dadc,#b9bcbf 50%,#8e9194)"></div>
  </div>

  <footer class="abs site-footer">
    <div class="f-col" style="left:91px">
      <h4>Kontaktuppgifter</h4>
      <div class="f-contact"><span class="dot"><svg width="8" height="8" viewBox="0 0 24 24"><path fill="#fff" d="M6.6 10.8a15.1 15.1 0 0 0 6.6 6.6l2.2-2.2a1 1 0 0 1 1-.25 11.4 11.4 0 0 0 3.6.57 1 1 0 0 1 1 1V20a1 1 0 0 1-1 1A17 17 0 0 1 3 4a1 1 0 0 1 1-1h3.5a1 1 0 0 1 1 1c0 1.25.2 2.45.57 3.57a1 1 0 0 1-.25 1z"/></svg></span><div><b>Telefon</b>+46 (0) 707 123 456</div></div>
      <div class="f-contact"><span class="dot"><svg width="8" height="8" viewBox="0 0 24 24"><path fill="none" stroke="#fff" stroke-width="2.4" d="M3 6h18v12H3zM3 6l9 7 9-7"/></svg></span><div><b>E-post</b>info@skyvane-demo.se</div></div>
    </div>
    <div class="f-col" style="left:257px">
      <h4>Partners</h4>
      <ul><li>Rotorplats</li><li>NHC</li><li>Lindas</li></ul>
    </div>
    <div class="f-col" style="left:365px">
      <h4>Länkar</h4>
      <ul><li>www.rotorplats-demo.se</li><li>www.rotorline-demo.com</li><li>www.norrvikflygklubb-demo.se/</li></ul>
    </div>
    <div class="f-col" style="left:513px">
      <h4>Öppetider</h4>
      <p style="margin-bottom:8px">Måndag – Söndag:<br>0900 – 1700</p>
      <p>Övrig tid enligt<br>överenskommelse.</p>
    </div>
    <div class="f-rule"></div>
    <div class="copyright">© 2022 SKYVANE. Alla Rättigheter Förbehållna.</div>
    <div class="f-social blue" style="left:549px"></div>
    <div class="f-social" style="left:569px"></div>
  </footer>

</body>
</html>
```